Lumen Ridge Puzzles Business Cards
Two-sided business cards
Professional
Pim Varlotte
Founder, KORV Fellow, Brellaquin MVP
pim@lumenridgepuzzles.example
www.lumenridgepuzzles.example
GPG Fingerprint: A2D1 5B09 F6C3 17E4 8D2A 40BC 9E71 3F58 C046
Logo to Use for Business Cards

```html
<!DOCTYPE html>
<html lang="en">
<head>
<meta charset="utf-8">
<title>Lumen Ridge Puzzles Stationery</title>
<link rel="stylesheet" href="https://fonts.googleapis.com/css2?family=Montserrat:wght@400;600;700&display=swap">
<style>
:root{
  --bg:#eeeeee;
  --paper:#ffffff;
  --ink:#333333;
  --rule:#9a9a9a;
  --brand:#1f5fae;
  --accent:#7cc242;
  --night:#0d0d0d;
  --tab-dark:#0a2c6e;
  --tab-light:#4fb0f0;
  --ghost:#dfe4ee;
}
*{box-sizing:border-box;margin:0;padding:0}
html,body{width:1200px;height:552px;overflow:hidden}
body{background:var(--bg);font-family:"Montserrat",sans-serif;color:var(--ink);position:relative}
.sheet,.card,.envelope{position:absolute;box-shadow:0 1px 3px rgba(0,0,0,.25)}
.sheet{background:var(--paper);top:12px;width:386px;height:528px}
.sheet--fax{left:12px}
.sheet--plain{left:410px;width:354px}
.brand{display:flex;align-items:center;gap:4px;font-weight:700;font-size:7px;letter-spacing:.4px;color:var(--brand);text-transform:uppercase;white-space:nowrap}
.brand__dot{width:7px;height:7px;border-radius:50%;background:var(--accent);flex:none}
.sheet .brand{position:absolute;top:14px;left:22px}
.fax-title{position:absolute;top:40px;right:22px;font-size:8px;font-weight:600}
.fax-table{position:absolute;top:50px;left:22px;width:342px;border-collapse:collapse;font-size:6px;table-layout:fixed}
.fax-table td{border:1px solid var(--rule);height:17px;padding:0 4px}
.fax-table .lbl{width:34px}
.checks{position:absolute;top:130px;left:22px;right:22px;display:flex;justify-content:space-between;font-size:5.5px}
.checks span{display:flex;align-items:center;gap:3px}
.checks i{width:7px;height:7px;border:1px solid var(--rule);display:inline-block}
.tab{position:absolute;top:215px;width:6px;height:80px;background:linear-gradient(180deg,var(--tab-light),var(--tab-dark) 50%,var(--tab-light))}
.tab--l{left:0;border-radius:0 4px 4px 0}
.tab--r{right:0;border-radius:4px 0 0 4px}
.ghost-name{position:absolute;font-weight:700;color:var(--ghost);text-transform:uppercase;text-align:center;line-height:1.1}
.sheet .ghost-name{top:410px;left:0;right:0;font-size:17px}
.footer{position:absolute;bottom:14px;left:0;right:0;text-align:center;font-size:4.5px;color:#777}
.card{background:var(--night);top:24px;height:79px;color:#ddd}
.card--info{left:785px;width:151px}
.card--logo{left:953px;width:122px}
.card--info .brand{position:absolute;top:10px;left:8px;width:56px;font-size:4.5px;white-space:normal;line-height:1.2}
.card__details{position:absolute;top:10px;left:72px;right:5px;font-size:3.4px;line-height:1.6;white-space:nowrap}
.card__details b{font-size:4.6px;color:#fff}
.card--logo .brand{position:absolute;top:34px;left:0;right:0;justify-content:center;font-size:6px}
.envelope{left:780px;width:408px;background:var(--night)}
.envelope--dark{top:115px;height:214px}
.envelope--dark .brand{position:absolute;top:20px;left:24px;font-size:5.5px}
.envelope__sender{position:absolute;top:34px;left:24px;font-size:4px;color:#aaa;line-height:1.5}
.window{position:absolute;left:24px;top:126px;width:124px;height:40px;background:var(--paper);border-radius:3px}
.envelope--dark .ghost-name{right:30px;top:80px;font-size:18px;color:#262626}
.envelope--light{top:341px;height:192px;background:var(--paper)}
.flap{position:absolute;top:0;left:0}
.envelope--light .brand{position:absolute;top:22px;left:0;right:0;justify-content:center;font-size:6px}
</style>
</head>
<body>

<section class="sheet sheet--fax">
  <div class="brand"><span class="brand__dot"></span>Lumen Ridge Puzzles</div>
  <div class="fax-title">FAX</div>
  <table class="fax-table">
    <tr><td class="lbl">To:</td><td></td><td class="lbl">From:</td><td></td></tr>
    <tr><td class="lbl">Fax:</td><td></td><td class="lbl">Pages:</td><td></td></tr>
    <tr><td class="lbl">Phone:</td><td></td><td class="lbl">Date:</td><td></td></tr>
    <tr><td class="lbl">Re:</td><td></td><td class="lbl">CC:</td><td></td></tr>
  </table>
  <div class="checks">
    <span><i></i>Urgent</span><span><i></i>For Review</span><span><i></i>Please Comment</span><span><i></i>Please Reply</span><span><i></i>Please Recycle</span>
  </div>
  <div class="tab tab--l"></div><div class="tab tab--r"></div>
  <div class="ghost-name">Lumen Ridge<br>Puzzles</div>
  <div class="footer">T +1 555 0142 &nbsp;·&nbsp; E pim@lumenridgepuzzles.example &nbsp;·&nbsp; W www.lumenridgepuzzles.example</div>
</section>

<section class="sheet sheet--plain">
  <div class="brand"><span class="brand__dot"></span>Lumen Ridge Puzzles</div>
  <div class="tab tab--l"></div><div class="tab tab--r"></div>
  <div class="ghost-name">Lumen Ridge<br>Puzzles</div>
  <div class="footer">T +1 555 0142 &nbsp;·&nbsp; E pim@lumenridgepuzzles.example &nbsp;·&nbsp; W www.lumenridgepuzzles.example</div>
</section>

<section class="card card--info">
  <div class="brand"><span class="brand__dot"></span><span>Lumen Ridge Puzzles</span></div>
  <div class="card__details">
    <b>Pim Varlotte</b><br>
    Founder, KORV Fellow, Brellaquin MVP<br>
    pim@lumenridgepuzzles.example<br>
    www.lumenridgepuzzles.example<br>
    GPG: A2D1 5B09 F6C3 17E4 8D2A<br>
    40BC 9E71 3F58 C046
  </div>
</section>

<section class="card card--logo">
  <div class="brand"><span class="brand__dot"></span>Lumen Ridge Puzzles</div>
</section>

<section class="envelope envelope--dark">
  <div class="brand"><span class="brand__dot"></span>Lumen Ridge Puzzles</div>
  <div class="envelope__sender">www.lumenridgepuzzles.example<br>pim@lumenridgepuzzles.example</div>
  <div class="window"></div>
  <div class="ghost-name">Lumen Ridge<br>Puzzles</div>
</section>

<section class="envelope envelope--light">
  <svg class="flap" width="408" height="60" viewBox="0 0 408 60" aria-hidden="true">
    <path d="M0 0H408V8L236 58Q204 64 172 58L0 8Z" fill="var(--night)"/>
  </svg>
  <div class="brand"><span class="brand__dot"></span>Lumen Ridge Puzzles</div>
</section>

</body>
</html>
```